Commercial Construction Company

We need a business card design based on our current logo. We are a commercial general contractor based in Southern California that specializes in bank remodels. We would like to see designs that incorporate dark blue. The final design should portray an image of professionalism and quality.

If possible, I would like to add metallic foil to the design. Thank you

```html
<!DOCTYPE html>
<html lang="en">
<head>
<meta charset="utf-8">
<title>Harlow Build Group – Business Card</title>
<link rel="stylesheet" href="https://fonts.googleapis.com/css2?family=Montserrat:wght@600;700;800&family=Open+Sans:wght@400;600&display=swap">
<style>
  :root {
    --stage: #262626;
    --ink: #0a0b0c;
    --navy: #0b4a80;
    --navy-bright: #1b5fa3;
    --silver: #a7a9ab;
    --white: #ffffff;
  }
  * { box-sizing: border-box; margin: 0; padding: 0; }
  html, body { width: 1200px; height: 900px; overflow: hidden; }
  body {
    background: var(--stage);
    font-family: "Open Sans", sans-serif;
    position: relative;
  }
  .card {
    position: absolute;
    left: 250px;
    width: 700px;
    height: 390px;
    background: var(--ink);
    overflow: hidden;
    box-shadow: 0 12px 30px rgba(0,0,0,.5);
  }
  .card--front { top: 40px; }
  .card--back { top: 470px; }
  .card__shapes { position: absolute; inset: 0; width: 100%; height: 100%; }

  .brand {
    position: absolute;
    display: flex;
    align-items: center;
    gap: 14px;
    font-family: "Montserrat", sans-serif;
    font-weight: 800;
    color: var(--white);
    letter-spacing: 2px;
  }
  .brand__dot {
    border-radius: 50%;
    background: var(--silver);
    flex: none;
  }
  .card--front .brand { right: 50px; top: 110px; font-size: 48px; }
  .card--front .brand__dot { width: 46px; height: 46px; }
  .card--back .brand { left: 370px; top: 55px; font-size: 42px; }
  .card--back .brand__dot { width: 40px; height: 40px; }

  .person {
    position: absolute;
    left: 380px;
    top: 210px;
    color: var(--white);
  }
  .person__name {
    font-family: "Montserrat", sans-serif;
    font-weight: 700;
    font-size: 24px;
    letter-spacing: 1px;
    color: var(--navy-bright);
    text-transform: uppercase;
    line-height: 1;
  }
  .person__role { font-size: 16px; line-height: 1.3; margin-top: 4px; }

  .contact {
    position: absolute;
    left: 360px;
    top: 266px;
    list-style: none;
    color: var(--white);
    font-size: 16px;
    line-height: 1.4;
  }
  .contact li { display: flex; align-items: center; gap: 10px; }
  .contact svg { width: 16px; height: 16px; flex: none; }
  .contact__domain { color: var(--navy-bright); }
  .contact__address { margin-top: 6px; }
</style>
</head>
<body>

  <section class="card card--front" aria-label="Card front">
    <svg class="card__shapes" viewBox="0 0 700 390" preserveAspectRatio="none" aria-hidden="true">
      <path d="M0 0 H700 V330 C520 330 300 260 150 0 Z" fill="var(--navy)"/>
      <path d="M700 300 C520 300 330 240 200 0" fill="none" stroke="var(--ink)" stroke-width="16"/>
    </svg>
    <div class="brand"><span class="brand__dot"></span><span>HARLOW</span></div>
  </section>

  <section class="card card--back" aria-label="Card back">
    <svg class="card__shapes" viewBox="0 0 700 390" preserveAspectRatio="none" aria-hidden="true">
      <rect x="0" y="0" width="700" height="150" fill="var(--navy)"/>
      <rect x="380" y="0" width="320" height="196" fill="var(--navy)"/>
      <line x1="0" y1="152" x2="380" y2="152" stroke="var(--white)" stroke-width="2"/>
      <line x1="380" y1="203" x2="700" y2="203" stroke="var(--navy-bright)" stroke-width="3"/>
    </svg>

    <div class="brand"><span class="brand__dot"></span><span>HARLOW</span></div>

    <div class="person">
      <p class="person__name">Daniel Mercer</p>
      <p class="person__role">Owner / CEO</p>
    </div>

    <ul class="contact">
      <li>
        <svg viewBox="0 0 16 16" aria-hidden="true"><path d="M4 1.5 L6.5 4.5 L5 6.5 C6 8.5 7.5 10 9.5 11 L11.5 9.5 L14.5 12 L12.5 14.5 C7 14 2 9 1.5 3.5 Z" fill="none" stroke="var(--navy-bright)" stroke-width="1.3"/></svg>
        <span>555 284 1937</span>
      </li>
      <li>
        <svg viewBox="0 0 16 16" aria-hidden="true"><rect x="1" y="3" width="14" height="10" fill="none" stroke="var(--navy-bright)" stroke-width="1.3"/><path d="M1 3 L8 9 L15 3" fill="none" stroke="var(--navy-bright)" stroke-width="1.3"/></svg>
        <span>info@harlowbuild.com</span>
      </li>
      <li>
        <svg viewBox="0 0 16 16" aria-hidden="true"><circle cx="8" cy="8" r="6.5" fill="none" stroke="var(--navy-bright)" stroke-width="1.3"/><ellipse cx="8" cy="8" rx="3" ry="6.5" fill="none" stroke="var(--navy-bright)" stroke-width="1.1"/><line x1="1.5" y1="8" x2="14.5" y2="8" stroke="var(--navy-bright)" stroke-width="1.1"/></svg>
        <span>www.<span class="contact__domain">harlowbuild</span>.com</span>
      </li>
      <li class="contact__address">Southern California 92804</li>
    </ul>
  </section>

</body>
</html>
```